Business acrd and Stationery desgin FOR HARLOW

I want creative and expressive stationary design .on the front side for business card I need the logo and doctors name to be there and on the back side I need time and appointment .Please see attached business card to use same names ,but use address below and phone number

Note:the deigner must submit the file in vector format and PSD and PDF

Business name is :Harlow Crest Medical Clinic.

Address:
20485 57 ST NW
City :EDMONTON AB
Postal code: T6K 3P8

Phone :(780) 492-3815
Fax:(780) 492-5127

Other Business name :Harlow Medical Clinic

• logo in the back on business card

```html
<!DOCTYPE html>
<html lang="en">
<head>
<meta charset="utf-8">
<title>Harlow Crest Medical Clinic – Business Card</title>
<link rel="stylesheet" href="https://fonts.googleapis.com/css2?family=Crimson+Pro:wght@400;600;700&family=Roboto:wght@400&display=swap">
<style>
  :root {
    --navy: #2a3f86;
    --red: #d42a36;
    --grey: #4a4a4a;
    --rule: #6b6b6b;
    --border: #8c8c8c;
    --paper: #ffffff;
    --tone-red: rgba(224, 96, 106, 0.55);
    --tone-blue: rgba(90, 111, 166, 0.5);
    --tone-sky: rgba(159, 203, 235, 0.45);
    --tone-red-faint: rgba(224, 96, 106, 0.12);
    --tone-blue-faint: rgba(90, 111, 166, 0.12);
  }
  * { margin: 0; padding: 0; box-sizing: border-box; }
  html, body { width: 1200px; height: 900px; overflow: hidden; background: var(--paper); }
  body { position: relative; font-family: "Crimson Pro", Georgia, serif; }

  .card {
    position: absolute;
    top: 262px;
    width: 534px;
    height: 308px;
    border: 1px solid var(--border);
    background: var(--paper);
    overflow: hidden;
  }
  .card--front { left: 46px; }
  .card--back { left: 626px; }

  .card__decor--front {
    position: absolute;
    left: 320px; top: 0;
    width: 214px; height: 308px;
    background:
      radial-gradient(ellipse 70% 55% at 45% 45%, var(--tone-red), transparent 70%),
      radial-gradient(ellipse 60% 60% at 75% 70%, var(--tone-blue), transparent 70%),
      radial-gradient(ellipse 50% 50% at 85% 85%, var(--tone-sky), transparent 70%);
  }
  .card__decor--back {
    position: absolute;
    inset: 0;
    background:
      radial-gradient(ellipse 60% 50% at 30% 80%, var(--tone-red-faint), transparent 75%),
      radial-gradient(ellipse 60% 60% at 80% 30%, var(--tone-blue-faint), transparent 75%);
  }

  .brand { position: absolute; left: 44px; top: 38px; display: flex; align-items: center; gap: 8px; }
  .brand__dot { width: 14px; height: 14px; border-radius: 50%; background: var(--red); }
  .brand__name { color: var(--navy); font-weight: 600; font-size: 20px; line-height: 1; letter-spacing: 0.3px; }

  .doctors { position: absolute; left: 44px; top: 117px; color: var(--navy); font-weight: 700; font-size: 20px; line-height: 24px; }

  .contact { position: absolute; left: 44px; top: 189px; color: var(--grey); font-size: 16.5px; line-height: 19.5px; display: flex; }
  .contact__address { width: 143px; font-style: normal; }
  .contact__phones span { display: inline-block; width: 36px; }

  .tagline { position: absolute; left: 44px; top: 266px; color: var(--red); font-size: 13.5px; }

  .appointments__title { position: absolute; top: 23px; width: 100%; text-align: center; color: var(--navy); font-weight: 600; font-size: 16.5px; }
  .appointments__list { position: absolute; left: 70px; top: 52px; list-style: none; }
  .appointments__row { display: flex; align-items: flex-end; height: 31.2px; color: var(--grey); font-size: 18px; }
  .appointments__num { width: 22px; }
  .appointments__line { display: inline-block; border-bottom: 1px solid var(--rule); height: 17px; }
  .appointments__line--date { width: 216px; }
  .appointments__line--time { width: 116px; }
  .appointments__at { width: 37px; text-align: center; }

  .notice { position: absolute; top: 267px; width: 100%; text-align: center; color: var(--red); font-size: 12.5px; }

  .size-label { position: absolute; top: 661px; width: 100%; text-align: center; font-family: "Roboto", Arial, sans-serif; font-size: 16px; color: #333; }
</style>
</head>
<body>

<section class="card card--front">
  <div class="card__decor--front" role="img" aria-label="Flowing red and blue ribbon artwork"></div>

  <div class="brand">
    <span class="brand__dot"></span>
    <span class="brand__name">Harlow Crest Medical Clinic</span>
  </div>

  <div class="doctors">
    <p>Dr. A. Morvane</p>
    <p>Dr. Z. Halloway</p>
  </div>

  <div class="contact">
    <address class="contact__address">
      20485 57 ST NW<br>Edmonton AB<br>T6K 3P8
    </address>
    <p class="contact__phones">
      <span>Tel</span>(780) 492-3815<br>
      <span>Fax</span>(780) 492-5127
    </p>
  </div>

  <p class="tagline">Family Doctors • Family Practice &amp; Walk-in Welcome</p>
</section>

<section class="card card--back">
  <div class="card__decor--back" role="img" aria-label="Faint red and blue ribbon artwork"></div>

  <h2 class="appointments__title">Your Next Appointment</h2>
  <ol class="appointments__list">
    <li class="appointments__row"><span class="appointments__num">1.</span><span class="appointments__line appointments__line--date"></span><span class="appointments__at">at</span><span class="appointments__line appointments__line--time"></span></li>
    <li class="appointments__row"><span class="appointments__num">2.</span><span class="appointments__line appointments__line--date"></span><span class="appointments__at">at</span><span class="appointments__line appointments__line--time"></span></li>
    <li class="appointments__row"><span class="appointments__num">3.</span><span class="appointments__line appointments__line--date"></span><span class="appointments__at">at</span><span class="appointments__line appointments__line--time"></span></li>
    <li class="appointments__row"><span class="appointments__num">4.</span><span class="appointments__line appointments__line--date"></span><span class="appointments__at">at</span><span class="appointments__line appointments__line--time"></span></li>
    <li class="appointments__row"><span class="appointments__num">5.</span><span class="appointments__line appointments__line--date"></span><span class="appointments__at">at</span><span class="appointments__line appointments__line--time"></span></li>
    <li class="appointments__row"><span class="appointments__num">6.</span><span class="appointments__line appointments__line--date"></span><span class="appointments__at">at</span><span class="appointments__line appointments__line--time"></span></li>
  </ol>

  <p class="notice">If you are unable to keep the appointment, kindly give at least 24 hours notice.</p>
</section>

<p class="size-label">9.5cm x 5.5cm</p>

</body>
</html>
```